Dental office stationary (letterhead, envelopes), business cards, presentation folders

Nothing too dental outside of the logo. I will need all stationary, presentation folders, business cards. Would prefer to stay in the colors of the logo

Gordon Pellham, DDS
Brightwell Dental Implant Center
555-555-0187
info@brightwelldental-example.com
3871 NW Corbin Rd Unit B
Marlowe Cove, FL 30000

Also need appointment date and time
And cancellation policy
I want it to say “kindly ask for
A 48hr cancellation policy to avoid incurring a cancellation fee”

Industry/Entity Type

Dental

Colors
0054AA
0677BA
7BADD7
CADEEF
E8F1F8

Requirements
Must have
• Name of your office, name of doctor, address, phone number
Should not have
• Too much tooth/dental. Only the tooth in logo

```html
<!DOCTYPE html>
<html lang="en">
<head>
<meta charset="utf-8">
<title>Brightwell Dental Implant Center — Business Card</title>
<link rel="stylesheet" href="https://fonts.googleapis.com/css2?family=Roboto:wght@400;500;700&display=swap">
<style>
  :root {
    --page: #2a2a2b;
    --card: #1f1f20;
    --blue-deep: #0a5cb4;
    --blue-bright: #14c3f0;
    --blue-line: #0b6fc4;
    --teal: #17b8a0;
    --brand: #16b0cf;
    --name: #19a6e2;
    --ink: #f4f6f8;
  }
  * { margin: 0; padding: 0; box-sizing: border-box; }
  html, body {
    width: 1200px; height: 900px; overflow: hidden;
    background: var(--page);
    font-family: "Roboto", Arial, sans-serif;
  }
  .business-card {
    position: absolute; left: 100px; top: 164px;
    width: 1000px; height: 571px;
    background: var(--card);
    overflow: hidden;
    box-shadow: 0 20px 50px rgba(0,0,0,.5);
  }
  .card-swoosh { position: absolute; inset: 0; width: 100%; height: 100%; }
  .brand-mark {
    position: absolute; right: 50px; top: 272px;
    display: flex; align-items: center; gap: 14px;
  }
  .brand-dot { width: 22px; height: 22px; border-radius: 50%; background: var(--brand); }
  .brand-name {
    color: var(--brand); font-weight: 500; font-size: 54px;
    letter-spacing: 3px; text-transform: uppercase; white-space: nowrap;
  }
  .doctor-block {
    position: absolute; right: 70px; top: 368px; text-align: right;
    color: var(--ink);
  }
  .doctor-name { color: var(--name); font-weight: 700; font-size: 27px; }
  .practice-name { font-size: 22px; margin-top: 4px; }
  .practice-address { font-size: 22px; line-height: 1.35; margin-top: 28px; }
  .contact-list {
    position: absolute; left: 58px; top: 392px; list-style: none;
    color: var(--ink); font-size: 22px;
  }
  .contact-item { display: flex; align-items: center; gap: 12px; line-height: 1.5; white-space: nowrap; }
  .contact-icon { width: 20px; height: 20px; flex: none; }
</style>
</head>
<body>
  <div class="business-card">
    <svg class="card-swoosh" viewBox="0 0 1000 571" preserveAspectRatio="none" aria-hidden="true">
      <defs>
        <linearGradient id="skyBand" x1="0" y1="0" x2="1" y2="0.3">
          <stop offset="0" stop-color="#0a5cb4"/>
          <stop offset="1" stop-color="#14c3f0"/>
        </linearGradient>
      </defs>
      <path d="M0,0 H1000 V70 C720,140 360,200 0,285 Z" fill="url(#skyBand)"/>
      <path d="M0,318 C330,225 700,175 1000,92" fill="none" stroke="#0b6fc4" stroke-width="7"/>
      <path d="M380,232 C640,205 860,150 1000,100 L1000,138 C860,190 640,225 380,232 Z" fill="#17b8a0"/>
    </svg>

    <div class="brand-mark">
      <span class="brand-dot"></span>
      <span class="brand-name">Brightwell</span>
    </div>

    <div class="doctor-block">
      <p class="doctor-name">Gordon Pellham, DDS</p>
      <p class="practice-name">Brightwell Dental Implant Center</p>
      <p class="practice-address">3871 NW Corbin Rd Unit B<br>Marlowe Cove, FL 30000</p>
    </div>

    <ul class="contact-list">
      <li class="contact-item">
        <svg class="contact-icon" viewBox="0 0 20 20" aria-hidden="true"><circle cx="10" cy="10" r="10" fill="#17b8a0"/><path d="M6 5c1 0 2 2 2 3l-1 1c1 2 2 3 4 4l1-1c1 0 3 1 3 2l-1 2c-5 0-10-5-10-10z" fill="#1f1f20"/></svg>
        555-555-0187
      </li>
      <li class="contact-item">
        <svg class="contact-icon" viewBox="0 0 20 20" aria-hidden="true"><circle cx="10" cy="10" r="10" fill="#17b8a0"/><rect x="4.5" y="6.5" width="11" height="7.5" fill="none" stroke="#1f1f20" stroke-width="1.5"/><path d="M4.5 6.5l5.5 4.5 5.5-4.5" fill="none" stroke="#1f1f20" stroke-width="1.5"/></svg>
        info@brightwelldental-example.com
      </li>
      <li class="contact-item">
        <svg class="contact-icon" viewBox="0 0 20 20" aria-hidden="true"><circle cx="10" cy="10" r="10" fill="#17b8a0"/><circle cx="10" cy="10" r="5.5" fill="none" stroke="#1f1f20" stroke-width="1.4"/><path d="M4.5 10h11M10 4.5c-3 3-3 8 0 11M10 4.5c3 3 3 8 0 11" fill="none" stroke="#1f1f20" stroke-width="1.2"/></svg>
        www.brightwelldental-example.com
      </li>
    </ul>
  </div>
</body>
</html>
```